need professional, precise design for a website

I will start with a homepage design and if we pick your design, we'll have you design up to 6 more interior pages (we'll pay extra for these of course). We need a homepage design for a reserve study company based in Idaho, covering the northwest region. The company is called copper ridge reserve study. Their current site is at https://www.copperridgereserves.example/ and they really like this site for inspiration https://www.fundplannerhub.example/ but they would like an original design, just more modern and fresh like the sample site. I have logo files I will attach. They want something that looks financial and has a feel of accuity. Their main call to action will be to have someone fill in a contact form or call them on the phone. They will have a sample study that someone can download as on the fundplannerhub site. You can use copy from their current site.

```html
<!DOCTYPE html>
<html lang="en">
<head>
<meta charset="utf-8">
<title>Copper Ridge Reserves — Reserve Studies for the Northwest</title>
<link href="https://fonts.googleapis.com/css2?family=Cinzel:wght@400;700&family=Open+Sans:wght@400;600&display=swap" rel="stylesheet">
<style>
:root{
  --navy:#1f1a4d;
  --navy-deep:#17133b;
  --purple:#2b2170;
  --purple-lite:#3e3193;
  --sky:#2b8fc9;
  --sky-deep:#1f6fa6;
  --grey:#efefef;
  --line:#d9d9de;
  --ink:#333;
  --muted:#666;
  --white:#fff;
}
*{box-sizing:border-box;margin:0;padding:0}
html,body{width:1200px;height:5172px;overflow:hidden}
body{font-family:"Open Sans",Arial,sans-serif;color:var(--ink);background:var(--white);position:relative}
section,header,footer{position:absolute;left:0;width:1200px}
.btn{display:inline-block;background:var(--navy);color:var(--white);font-family:"Cinzel",Georgia,serif;font-size:14px;letter-spacing:1px;padding:12px 22px;text-decoration:none}

/* header */
.site-header{top:0;height:130px;background:var(--white)}
.topbar{position:absolute;top:0;left:0;width:1200px;height:45px;background:#e9e9ec}
.topbar .btn{position:absolute;top:0;height:45px;padding:14px 20px;font-size:13px}
.topbar .portal{left:733px}
.topbar .proposal{left:873px}
.brand{position:absolute;left:190px;top:55px;display:flex;align-items:center;gap:12px;font-family:"Cinzel",Georgia,serif;font-size:26px;color:var(--navy);letter-spacing:.5px}
.brand .mark{width:26px;height:26px;border:2px solid var(--navy);border-radius:50%}
.nav{position:absolute;right:172px;top:86px;display:flex;gap:34px;font-family:"Cinzel",Georgia,serif;font-size:13px;color:var(--navy);letter-spacing:.5px}

/* hero */
.hero{top:130px;height:645px}
.hero .photo{position:absolute;inset:0;background:linear-gradient(180deg,#3a4e7a 0%,#7d7f9a 30%,#b9a283 52%,#8a6e3e 70%,#4a4a30 100%)}
.hero h1{position:absolute;top:110px;width:100%;text-align:center;color:var(--white);font-family:"Cinzel",Georgia,serif;font-weight:400;font-size:34px;line-height:44px;letter-spacing:1px}
.hero .call{position:absolute;top:210px;left:478px;font-size:17px;padding:13px 26px}
.hero .dots{position:absolute;top:595px;left:570px;display:flex;gap:9px}
.hero .dots i{width:10px;height:10px;border-radius:50%;background:rgba(255,255,255,.7)}
.hero .dots i:first-child{background:var(--white)}
.hero svg{position:absolute;bottom:0;left:0}

/* stats */
.stats{top:775px;height:495px;background:var(--grey);text-align:center}
.stats .lead{position:absolute;top:128px;left:0;width:100%;font-family:"Cinzel",Georgia,serif;font-size:17px;line-height:32px;color:var(--navy);letter-spacing:.5px}
.stat-row{position:absolute;top:250px;left:215px;width:770px;display:flex;justify-content:space-between}
.stat{width:230px;color:var(--navy)}
.stat b{display:block;font-family:"Cinzel",Georgia,serif;font-weight:400;font-size:70px;line-height:74px}
.stat b sup{font-size:34px;vertical-align:24px}
.stat span{display:block;font-family:"Cinzel",Georgia,serif;font-size:13px;line-height:18px;color:#555;margin-top:6px;letter-spacing:.5px}

/* welcome */
.welcome{top:1270px;height:578px}
.welcome h2{position:absolute;left:172px;top:115px;font-family:"Cinzel",Georgia,serif;font-weight:400;font-size:25px;line-height:30px;color:var(--navy)}
.welcome p{position:absolute;left:172px;top:190px;width:300px;font-size:12px;line-height:21px;color:var(--muted)}
.welcome .btn{position:absolute;left:172px;top:398px}
.welcome .photo{position:absolute;left:588px;top:116px;width:438px;height:324px;background:linear-gradient(180deg,#cfe0ee 0%,#a7bfd4 40%,#9aa0a4 70%,#5d7b4c 100%)}

/* properties */
.properties{top:1848px;height:680px;background:linear-gradient(135deg,var(--purple) 0%,var(--navy-deep) 60%,var(--purple-lite) 100%)}
.properties h2{position:absolute;top:82px;left:0;width:100%;text-align:center;font-family:"Cinzel",Georgia,serif;font-weight:400;font-size:23px;color:var(--white);letter-spacing:1px}
.cards{position:absolute;top:164px;left:172px;width:856px;display:grid;grid-template-columns:repeat(4,200px);gap:28px 18px}
.card{height:183px;background:var(--white);border-radius:4px;text-align:center;padding-top:34px}
.card svg{width:60px;height:52px;stroke:var(--navy);fill:none;stroke-width:2}
.card h3{margin-top:14px;font-family:"Cinzel",Georgia,serif;font-weight:400;font-size:11.5px;line-height:17px;color:var(--navy);padding:0 14px}

/* region */
.region{top:2528px;height:637px}
.region .map{position:absolute;left:172px;top:104px;width:475px;height:440px;background:var(--white);box-shadow:0 0 18px rgba(0,0,0,.12);padding:28px}
.region .map .fill{width:100%;height:100%;background:linear-gradient(160deg,#9fc0df 0%,#6f9bc8 55%,#4e7fb3 100%)}
.region h2{position:absolute;left:690px;top:172px;font-family:"Cinzel",Georgia,serif;font-weight:400;font-size:21px;line-height:27px;color:var(--navy)}
.region p{position:absolute;left:690px;top:245px;width:340px;font-size:12px;line-height:21px;color:var(--muted)}
.region .btn{position:absolute;left:690px;top:442px}

/* banner */
.banner{top:3165px;height:351px;background:linear-gradient(180deg,var(--sky) 0%,var(--sky-deep) 100%);text-align:center}
.banner .scene{position:absolute;inset:0;background:linear-gradient(180deg,rgba(255,255,255,0) 40%,rgba(255,255,255,.12) 100%)}
.banner h2{position:absolute;top:90px;left:0;width:100%;font-family:"Cinzel",Georgia,serif;font-weight:400;font-size:22px;line-height:32px;color:var(--white);letter-spacing:.5px}
.banner .ghost{position:absolute;top:180px;left:482px;border:1px solid rgba(255,255,255,.8);background:transparent;font-size:13px;padding:9px 20px}

/* news */
.news{top:3516px;height:646px}
.news h2{position:absolute;top:72px;left:0;width:100%;text-align:center;font-family:"Cinzel",Georgia,serif;font-weight:400;font-size:27px;color:var(--navy);letter-spacing:1px}
.posts{position:absolute;top:160px;left:172px;display:flex;gap:25px}
.post{width:268px;height:404px;border:1px solid var(--line)}
.post .photo{height:193px}
.post:nth-child(1) .photo{background:linear-gradient(180deg,#9bb7cf,#c49a5a 55%,#6a7d3b)}
.post:nth-child(2) .photo{background:linear-gradient(180deg,#5f95c9,#5f8a4c 55%,#6cb3c9)}
.post:nth-child(3) .photo{background:linear-gradient(180deg,#7f9a56,#5a5e4c 50%,#3f4f2e)}
.post h3{margin:30px 14px 0;font-family:"Cinzel",Georgia,serif;font-weight:400;font-size:13px;line-height:19px;color:var(--navy)}
.post p{margin:8px 14px 0;font-size:11px;line-height:17px;color:var(--muted)}
.post .btn{margin:16px 0 0 14px;font-size:12px;padding:9px 18px}

/* testimonials */
.testimonials{top:4162px;height:362px;background:var(--grey);text-align:center}
.testimonials h2{position:absolute;top:82px;left:0;width:100%;font-family:"Cinzel",Georgia,serif;font-weight:400;font-size:25px;color:var(--navy);letter-spacing:1px}
.testimonials blockquote{position:absolute;top:170px;left:300px;width:600px;font-size:13px;line-height:24px;font-style:italic;color:#777}
.testimonials blockquote .q{font-family:"Cinzel",Georgia,serif;font-size:40px;color:#888;font-style:normal;vertical-align:-14px;line-height:0}
.testimonials cite{position:absolute;top:292px;left:0;width:100%;display:block;text-align:center;font-family:"Cinzel",Georgia,serif;font-style:normal;font-size:12px;color:var(--navy)}

/* contact */
.contact{top:4524px;height:506px;background:linear-gradient(180deg,var(--purple) 0%,var(--navy) 100%);color:var(--white);text-align:center}
.contact .wave{position:absolute;top:0;left:0}
.contact h2{position:absolute;top:108px;left:0;width:100%;font-family:"Cinzel",Georgia,serif;font-weight:400;font-size:25px;letter-spacing:1px}
.contact .intro{position:absolute;top:150px;left:320px;width:560px;font-size:12px;line-height:20px;color:#dcdaf0}
.contact form{position:absolute;top:250px;left:172px;width:856px;height:200px}
.field{position:absolute;left:0;width:412px;height:32px;border:1px solid rgba(255,255,255,.7);text-align:left;padding:7px 10px;font-size:12px;color:#e8e6f5}
.field.msg{left:438px;top:0;width:412px;height:140px}
.submit{position:absolute;left:734px;top:176px;background:var(--white);color:var(--navy);font-family:"Cinzel",Georgia,serif;font-size:13px;padding:10px 24px}

/* footer */
.site-footer{top:5030px;height:142px;background:var(--navy-deep);color:#c9c7dc}
.social{position:absolute;left:172px;top:45px;display:flex;gap:22px}
.social i{width:18px;height:18px;border-radius:50%;background:var(--white)}
.copy{position:absolute;left:172px;top:88px;font-size:11px}
.footer-brand{position:absolute;left:757px;top:40px;display:flex;align-items:center;gap:12px;font-family:"Cinzel",Georgia,serif;font-size:24px;color:#dcdaf0}
.footer-brand .mark{width:34px;height:34px;border:2px solid #dcdaf0;border-radius:50%}
</style>
</head>
<body>

<header class="site-header">
  <div class="topbar">
    <a class="btn portal" href="#">CLIENT PORTAL</a>
    <a class="btn proposal" href="#">REQUEST A PROPOSAL</a>
  </div>
  <div class="brand"><span class="mark"></span>Copper Ridge Reserves</div>
  <nav class="nav"><span>HOME</span><span>ABOUT OUR COMPANY</span><span>RESERVE STUDIES</span><span>CONTACT US</span></nav>
</header>

<section class="hero">
  <div class="photo" role="img" aria-label="Photograph of the downtown Boise skyline at dusk with autumn trees"></div>
  <h1>YOUR FINANCIAL ROAD<br>MAP FOR THE NEXT 30 YEARS!</h1>
  <a class="btn call" href="#">CALL (208) 555-0143</a>
  <div class="dots"><i></i><i></i><i></i><i></i></div>
  <svg width="1200" height="150" viewBox="0 0 1200 150" aria-hidden="true">
    <path d="M0 40 Q600 170 1200 40 L1200 150 L0 150 Z" fill="#efefef"/>
    <path d="M160 112 Q600 175 1040 112 Q600 150 160 112 Z" fill="#1f1a4d"/>
    <path d="M0 40 Q600 170 1200 40 L1200 48 Q600 178 0 48 Z" fill="#fff"/>
  </svg>
</section>

<section class="stats">
  <p class="lead">EACH YEAR, THOUSANDS OF MANAGERS, BOARD MEMBERS, AND<br>FACILITY DIRECTORS TRUST US TO CREATE THEIR RESERVE FUNDING PLANS</p>
  <div class="stat-row">
    <div class="stat"><b>30</b><span>YEARS<br>EXPERIENCE</span></div>
    <div class="stat"><b>40,000</b><span>RESERVE STUDIES<br>COMPLETED</span></div>
    <div class="stat"><b><sup>$</sup>300</b><span>MILLION FUNDING<br>GUIDANCE PROVIDED</span></div>
  </div>
</section>

<section class="welcome">
  <h2>WELCOME TO<br>COPPER RIDGE RESERVES</h2>
  <p>A copper ridge stands steady on the horizon, a landmark travelers have relied on for centuries. Reading that ridge line is much like reading the long view of a reserve fund. With so many costs ahead and a seemingly endless list of components, it helps to have a fixed point. Amid the constellations and distractions of daily budgets, Copper Ridge remains ever true, ever vigilant and ever rooted.</p>
  <a class="btn" href="#">READ MORE</a>
  <div class="photo" role="img" aria-label="Photograph of a high-rise condominium tower against a blue sky"></div>
</section>

<section class="properties">
  <h2>WE WORK WITH ALL TYPES OF PROPERTIES</h2>
  <div class="cards">
    <div class="card"><svg viewBox="0 0 60 52"><path d="M6 24 30 6 54 24M12 20v28h36V20M24 48V34h12v14"/></svg><h3>HOA &amp; CONDOMINIUM STUDIES</h3></div>
    <div class="card"><svg viewBox="0 0 60 52"><path d="M16 48V10h28v38M8 48h44M22 16h4M34 16h4M22 26h4M34 26h4M26 48V38h8v10"/></svg><h3>COMMERCIAL, VACATION &amp; TIME SHARE</h3></div>
    <div class="card"><svg viewBox="0 0 60 52"><path d="M6 22 30 6 54 22M10 22h40M14 22v22M24 22v22M36 22v22M46 22v22M8 48h44"/></svg><h3>MUNICIPALITIES PROPERTIES</h3></div>
    <div class="card"><svg viewBox="0 0 60 52"><circle cx="40" cy="14" r="7"/><path d="M40 21v27M8 48h44M14 48V34l8-6 8 6v14"/></svg><h3>PARKS &amp; PUBLIC LANDS</h3></div>
    <div class="card"><svg viewBox="0 0 60 52"><path d="M6 48h48M10 48V22h40v26M18 22 30 10l12 12M26 48V36h8v12M30 4v6"/></svg><h3>SCHOOLS, COLLEGES &amp; UNIVERSITIES</h3></div>
    <div class="card"><svg viewBox="0 0 60 52"><path d="M18 6 8 26h20L18 6M18 26v22M42 10 32 34h20L42 10M42 34v14M4 48h52"/></svg><h3>CAMPS &amp; RETREATS ORGANIZATIONS</h3></div>
    <div class="card"><svg viewBox="0 0 60 52"><path d="M14 44 44 10M40 8l8 6M8 48h44M34 40a6 6 0 1 0 0.1 0"/></svg><h3>PRIVATE CLUBS &amp; RECREATION CENTERS</h3></div>
    <div class="card"><svg viewBox="0 0 60 52"><path d="M8 26 30 8l22 18M14 22v26h32V22M26 48V34h8v14"/></svg><h3>OTHER TYPES OF PROPERTIES</h3></div>
  </div>
</section>

<section class="region">
  <div class="map"><div class="fill" role="img" aria-label="Map of Idaho counties in shades of blue"></div></div>
  <h2>IDAHO<br>NORTHWEST REGION</h2>
  <p>We serve associations and facility owners across Idaho and the wider Northwest, from the Panhandle to the Snake River Plain. Each study begins with a careful site visit and ends with a clear funding plan that boards can read, trust and act on without guesswork. Local knowledge keeps our estimates grounded in regional costs.</p>
  <a class="btn" href="#">CASE STUDY</a>
</section>

<section class="banner">
  <div class="scene" role="img" aria-label="Soft blue illustration of a park with trees and people walking"></div>
  <h2>OUR REPORT COVERS A ONE-YEAR PERIOD AND<br>INCLUDES A 30-YEAR CASH FLOW FORECAST</h2>
  <a class="btn ghost" href="#">READ SAMPLE RESERVE STUDY</a>
</section>

<section class="news">
  <h2>LATEST NEWS</h2>
  <div class="posts">
    <article class="post"><div class="photo" role="img" aria-label="Photograph of a community playground"></div><h3>PLANNING AHEAD FOR<br>PLAYGROUND REPAIRS</h3><p>Simple steps that keep shared play areas safe and funded.</p><a class="btn" href="#">READ MORE</a></article>
    <article class="post"><div class="photo" role="img" aria-label="Photograph of a resort pool with palm trees"></div><h3>WHAT A POOL RESURFACE<br>REALLY COSTS</h3><p>Timing and budgeting for your next pool renovation project.</p><a class="btn" href="#">READ MORE</a></article>
    <article class="post"><div class="photo" role="img" aria-label="Photograph of a stone fountain in a garden"></div><h3>CARING FOR FOUNTAINS<br>AND WATER FEATURES</h3><p>Why water features belong on every component inventory list.</p><a class="btn" href="#">READ MORE</a></article>
  </div>
</section>

<section class="testimonials">
  <h2>WHAT OUR CUSTOMERS SAY</h2>
  <blockquote><span class="q">“</span> Their team walked our board through every line of the study and made a thirty-year plan feel simple. We finally have a funding schedule our owners understand and support, and no surprise assessments. <span class="q">”</span></blockquote>
  <cite>- DANA WHITFIELD, BOISE</cite>
</section>

<section class="contact">
  <svg class="wave" width="1200" height="90" viewBox="0 0 1200 90" aria-hidden="true">
    <path d="M0 0H1200V40Q600 -30 0 40Z" fill="#efefef"/>
    <path d="M140 52Q600 -10 1060 52Q600 14 140 52Z" fill="#fff"/>
  </svg>
  <h2>CONTACT US</h2>
  <p class="intro">Tell us about your property and we will reply within one business day with a proposal and a clear timeline for your study.</p>
  <form>
    <div class="field" style="top:0">Name:</div>
    <div class="field" style="top:54px">Email:</div>
    <div class="field" style="top:108px">Phone:</div>
    <div class="field msg">Message:</div>
    <span class="submit">SUBMIT</span>
  </form>
</section>

<footer class="site-footer">
  <div class="social"><i></i><i></i><i></i><i></i></div>
  <p class="copy">Copyright Copper Ridge Reserves, LLC © 2019. All Rights Are Reserved.</p>
  <div class="footer-brand"><span class="mark"></span>Copper Ridge Reserves</div>
</footer>

</body>
</html>
```